1" x 3" label needed for essential oil bottle(s) - new ecommerce company

We need a label designed for 10 ml bottles of essential oils. We are offering 9 different types of essential oil: Lavender, Cedarwood, Eucalyptus, Frankincense, Lemon, Orange, Peppermint, Rosemary, and Tea Tree. The label should have a space for the type of essential oil. The bottles are an amber color (am including a photo) as essential oils are sensitive to light. also am including an AI file of our logo, which we'd like included on the label; the logo file also contains our logo colors, a dark blue and light grey. We'd also like the following on the label: "CAUTION: EYE AND SKIN IRRITANT. Avoid contact with eyes and skin. Wash hands after handling. If eye contact occurs, flush with water for 15 minutes. Not intended for topical or internal use. Contains Essential Oils. KEEP OUT OF REACH OF CHILDREN."
Also "Ingredients: 100% pure essential oil, GC tested."
Also "0.33 fl oz (10 ml)
Finally, we will need to include a sideways bar code on the right side of the label, so need 3/8" of white space on the right of the label.
We'd like the label to be calming, but modern, friendly, and confident.

```html
<!DOCTYPE html>
<html lang="en">
<head>
<meta charset="utf-8">
<title>Solenne Essential Oil Labels</title>
<link rel="stylesheet" href="https://fonts.googleapis.com/css2?family=Montserrat:wght@500&family=Zilla+Slab:wght@500;600&family=Barlow+Semi+Condensed:wght@400;700&family=Tinos:wght@400&display=swap">
<style>
  :root{
    --page:#ffffff;
    --label-white:#f4f4f4;
    --ink-grey:#5b6168;
    --brand-purple:#4e3680;
    --text-purple:#3f2d78;
    --lavender:#4e3680;
    --eucalyptus:#2f8f3c;
    --teatree:#3a9d34;
    --cedarwood:#8a5a50;
    --frankincense:#cf9156;
    --rosemary:#e24a7a;
    --lemon:#c99a1f;
    --orange:#cb6f1c;
    --peppermint:#c9a130;
    --gold-text:#c9a230;
    --white:#ffffff;
  }
  *{box-sizing:border-box;margin:0;padding:0}
  html,body{width:800px;height:1200px;overflow:hidden;background:var(--page)}
  .canvas{position:relative;width:800px;height:1200px}

  /* front panels */
  .front{position:absolute;width:117px;height:172px;overflow:hidden;color:var(--band);
    background:linear-gradient(90deg,#e9e9e9,var(--label-white) 40%,#ececec)}
  .front svg.band{position:absolute;left:0;top:0}
  .front .brand{position:absolute;left:0;width:117px;top:40px;display:flex;align-items:center;justify-content:center;gap:5px;font:500 15px/1 "Zilla Slab",serif;color:var(--ink-grey)}
  .front .brand .dot{width:9px;height:9px;border-radius:50%;background:var(--ink-grey)}
  .front .tagline{position:absolute;left:0;width:117px;top:66px;text-align:center;font:500 4.4px/1 "Montserrat",sans-serif;letter-spacing:.8px;color:var(--ink-grey)}
  .front .oil{position:absolute;left:13px;top:100px;font:600 14px/1 "Zilla Slab",serif;color:var(--white);white-space:nowrap}
  .front .oil.small{font-size:11.5px;top:103px}
  .front .kind{position:absolute;left:13px;top:119px;font:400 9.5px/1 "Zilla Slab",serif;color:var(--white);opacity:.92}
  .front .volume{position:absolute;left:13px;top:154px;font:400 6.5px/1 "Tinos",serif;color:var(--white)}
  .front .pure{position:absolute;left:71px;top:131px;width:34px;text-align:center;font:400 8px/0.95 "Tinos",serif;color:var(--gold-text)}

  /* flat back label */
  .label{position:absolute;left:66px;top:847px;width:668px;height:222px;background:var(--white);box-shadow:0 1px 6px rgba(0,0,0,.18);overflow:hidden}
  .label svg.band{position:absolute;left:0;top:0}
  .caution-title{position:absolute;left:20px;top:12px;font:700 13.5px/1 "Barlow Semi Condensed",sans-serif;color:var(--text-purple);letter-spacing:-.2px}
  .caution-text{position:absolute;left:20px;top:31px;width:185px;font:400 11.3px/16px "Barlow Semi Condensed",sans-serif;color:var(--text-purple);text-align:justify}
  .keep-out{position:absolute;left:48px;top:143px;width:127px;height:56px;border:2px solid var(--white);border-radius:7px;display:flex;align-items:center;justify-content:center;text-align:center;font:700 12px/17px "Barlow Semi Condensed",sans-serif;color:var(--white)}
  .center-brand{position:absolute;left:234px;width:200px;top:54px;display:flex;align-items:center;justify-content:center;gap:7px;font:500 22px/1 "Zilla Slab",serif;color:var(--text-purple)}
  .center-brand .dot{width:13px;height:13px;border-radius:50%;background:var(--text-purple)}
  .center-tagline{position:absolute;left:234px;width:200px;top:90px;text-align:center;font:500 5.8px/1 "Montserrat",sans-serif;letter-spacing:1.4px;color:var(--text-purple)}
  .label .oil{position:absolute;left:268px;top:124px;font:600 20px/1 "Zilla Slab",serif;color:var(--white)}
  .label .kind{position:absolute;left:268px;top:148px;font:400 13px/1 "Zilla Slab",serif;color:var(--white)}
  .label .volume{position:absolute;left:268px;top:204px;font:400 9px/1 "Tinos",serif;color:var(--white)}
  .label .pure{position:absolute;left:348px;top:168px;width:52px;text-align:center;font:400 11.5px/0.95 "Tinos",serif;color:var(--gold-text)}
  .ingredients-title{position:absolute;left:466px;top:12px;font:700 13.5px/1 "Barlow Semi Condensed",sans-serif;color:var(--text-purple)}
  .ingredients-text{position:absolute;left:466px;top:31px;width:96px;font:400 11.3px/16px "Barlow Semi Condensed",sans-serif;color:var(--text-purple)}
  .distributor{position:absolute;left:466px;top:146px;font:400 8.4px/12px "Barlow Semi Condensed",sans-serif;color:var(--white)}
  .distributor strong{font-weight:700}
  .icons{position:absolute;left:466px;top:187px}
  .barcode-space{position:absolute;left:565px;top:0;width:84px;height:210px;background:var(--white)}
</style>
</head>
<body>
<div class="canvas">
  <svg width="0" height="0" style="position:absolute">
    <defs>
      <linearGradient id="drop-fill" x1="0" y1="0" x2="0" y2="1">
        <stop offset="0" stop-color="#f6d24a"/>
        <stop offset=".55" stop-color="#fbe890"/>
        <stop offset="1" stop-color="#f2cd45"/>
      </linearGradient>
      <symbol id="front-band" viewBox="0 0 117 172">
        <path d="M0 89 H66 C76 89 80 92 84 96 C87 92 92 89 100 89 H117 V172 H0 Z" fill="currentColor"/>
        <path d="M88 94 C92 108 106 120 106 137 A18 18 0 0 1 70 137 C70 120 84 108 88 94 Z" fill="url(#drop-fill)" stroke="#ffffff" stroke-width="2.5"/>
        <ellipse cx="88" cy="161" rx="17" ry="2" fill="#000" opacity=".18"/>
      </symbol>
    </defs>
  </svg>

  <!-- row one -->
  <div class="front" style="left:68px;top:262px;--band:var(--lavender)">
    <svg class="band" width="117" height="172"><use href="#front-band"/></svg>
    <div class="brand"><span class="dot"></span>SOLENNE</div><div class="tagline">CALM BOTANICAL ESSENTIALS</div>
    <div class="oil">Lavender</div><div class="kind">essential oil</div><div class="pure">100%<br>PURE</div><div class="volume">0.33 fl oz (10 ml)</div>
  </div>
  <div class="front" style="left:207px;top:262px;--band:var(--eucalyptus)">
    <svg class="band" width="117" height="172"><use href="#front-band"/></svg>
    <div class="brand"><span class="dot"></span>SOLENNE</div><div class="tagline">CALM BOTANICAL ESSENTIALS</div>
    <div class="oil small">Eucalyptus</div><div class="kind">essential oil</div><div class="pure">100%<br>PURE</div><div class="volume">0.33 fl oz (10 ml)</div>
  </div>
  <div class="front" style="left:344px;top:262px;--band:var(--teatree)">
    <svg class="band" width="117" height="172"><use href="#front-band"/></svg>
    <div class="brand"><span class="dot"></span>SOLENNE</div><div class="tagline">CALM BOTANICAL ESSENTIALS</div>
    <div class="oil">Tea Tree</div><div class="kind">essential oil</div><div class="pure">100%<br>PURE</div><div class="volume">0.33 fl oz (10 ml)</div>
  </div>
  <div class="front" style="left:483px;top:262px;--band:var(--cedarwood)">
    <svg class="band" width="117" height="172"><use href="#front-band"/></svg>
    <div class="brand"><span class="dot"></span>SOLENNE</div><div class="tagline">CALM BOTANICAL ESSENTIALS</div>
    <div class="oil small">Cedarwood</div><div class="kind">essential oil</div><div class="pure">100%<br>PURE</div><div class="volume">0.33 fl oz (10 ml)</div>
  </div>
  <div class="front" style="left:620px;top:262px;--band:var(--frankincense)">
    <svg class="band" width="117" height="172"><use href="#front-band"/></svg>
    <div class="brand"><span class="dot"></span>SOLENNE</div><div class="tagline">CALM BOTANICAL ESSENTIALS</div>
    <div class="oil small" style="font-size:10px">Frankincense</div><div class="kind">essential oil</div><div class="pure">100%<br>PURE</div><div class="volume">0.33 fl oz (10 ml)</div>
  </div>

  <!-- row two -->
  <div class="front" style="left:130px;top:598px;--band:var(--rosemary)">
    <svg class="band" width="117" height="172"><use href="#front-band"/></svg>
    <div class="brand"><span class="dot"></span>SOLENNE</div><div class="tagline">CALM BOTANICAL ESSENTIALS</div>
    <div class="oil small" style="font-size:13px">Rosemary</div><div class="kind">essential oil</div><div class="pure">100%<br>PURE</div><div class="volume">0.33 fl oz (10 ml)</div>
  </div>
  <div class="front" style="left:267px;top:598px;--band:var(--lemon)">
    <svg class="band" width="117" height="172"><use href="#front-band"/></svg>
    <div class="brand"><span class="dot"></span>SOLENNE</div><div class="tagline">CALM BOTANICAL ESSENTIALS</div>
    <div class="oil">Lemon</div><div class="kind">essential oil</div><div class="pure">100%<br>PURE</div><div class="volume">0.33 fl oz (10 ml)</div>
  </div>
  <div class="front" style="left:406px;top:598px;--band:var(--orange)">
    <svg class="band" width="117" height="172"><use href="#front-band"/></svg>
    <div class="brand"><span class="dot"></span>SOLENNE</div><div class="tagline">CALM BOTANICAL ESSENTIALS</div>
    <div class="oil">Orange</div><div class="kind">essential oil</div><div class="pure">100%<br>PURE</div><div class="volume">0.33 fl oz (10 ml)</div>
  </div>
  <div class="front" style="left:543px;top:598px;--band:var(--peppermint)">
    <svg class="band" width="117" height="172"><use href="#front-band"/></svg>
    <div class="brand"><span class="dot"></span>SOLENNE</div><div class="tagline">CALM BOTANICAL ESSENTIALS</div>
    <div class="oil small">Peppermint</div><div class="kind">essential oil</div><div class="pure">100%<br>PURE</div><div class="volume">0.33 fl oz (10 ml)</div>
  </div>

  <!-- full wrap label -->
  <div class="label">
    <svg class="band" width="668" height="222" viewBox="0 0 668 222">
      <path d="M0 118 H356 C364 118 368 122 372 126 C376 122 380 118 388 118 H668 V222 H0 Z" fill="var(--brand-purple)"/>
      <path d="M373 122 C380 142 400 158 400 182 A27 27 0 0 1 346 182 C346 158 366 142 373 122 Z" fill="url(#drop-fill)" stroke="#ffffff" stroke-width="3"/>
      <ellipse cx="373" cy="212" rx="27" ry="2.5" fill="#000" opacity=".22"/>
    </svg>
    <div class="caution-title">CAUTION: EYE AND SKIN IRRITANT</div>
    <p class="caution-text">Avoid contact with eyes and skin. Wash hands after handling. If eye contact occurs, flush with water for 15 minutes. Not intended for topical or internal use. Contains Essential Oils.</p>
    <div class="keep-out">KEEP OUT OF REACH<br>OF CHILDREN</div>

    <div class="center-brand"><span class="dot"></span>SOLENNE</div>
    <div class="center-tagline">CALM BOTANICAL ESSENTIALS</div>
    <div class="oil">Lavender</div>
    <div class="kind">essential oil</div>
    <div class="pure">100%<br>PURE</div>
    <div class="volume">0.33 fl oz (10 ml)</div>

    <div class="ingredients-title">INGREDIENTS:</div>
    <p class="ingredients-text">100% pure essential oil, GC tested.</p>
    <div class="distributor"><strong>Distributed by:</strong><br>Lorem ipsum dolor sit amet</div>
    <svg class="icons" width="60" height="26" viewBox="0 0 60 26" aria-label="Recycle and 36 month shelf life icons">
      <path d="M13 3 L24 21 H2 Z" fill="none" stroke="#fff" stroke-width="3" stroke-linejoin="round"/>
      <rect x="37" y="10" width="20" height="12" rx="2" fill="none" stroke="#fff" stroke-width="1.2"/>
      <path d="M38 9 L54 2" stroke="#fff" stroke-width="1.2"/>
      <text x="47" y="19.5" text-anchor="middle" font-family="Barlow Semi Condensed, sans-serif" font-weight="700" font-size="8" fill="#fff">36M</text>
    </svg>
    <div class="barcode-space"></div>
  </div>
</div>
</body>
</html>
```